House-share and Room Rental Website (With Focus on the Bedroom Landing Page)

Looking for website design for our House-share (executive accommodation) and room rental business.

Our company name is: Lodvenra could also be written as LodVenra or lodvenra. Either is fine .. just looking for a nice clean catchy logo to go with the design.

EXAMPLES
These are examples of other websites in this field that are doing well. this is a kind of baseline.
https://kelbrin.com.au/
https://www.tuvaplex.com/
https://www.nestorvi.com/
https://www.quillsa.net/
https://www.pendlebarrow.com.au/

Our business model is to rent rooms to people looking for high-quality accommodation. We fill the gap between those looking to rent rooms and those with rooms to rent. However, our model is slightly different from those already on the market as we looking to fill a massive gap in the market delivering upmarket rooms for rent.(Executive Accommodation) also in the back end will be coupled with a self management process in the back end.

We offer executive style accommodation that stands out above the rest. With special extras like fire safety.. and management processes that create happier homes. We are looking for a web design package that can help us grow and scale our business. We need a design that is captivating

Our MAIN focus is having a room landing page that stands out from the rest... The core of our business will rely on the promotion of the rooms in a share house... so the whole design relies on the BEDROOM landing page to drive results.

Target Market(s)

We have 2 markets we are aiming at ... the first market is people offering rooms to rent who want the highest rental return. The second market is people looking to rent safe, high-quality rooms, in houses that are well managed and looked after.

Industry/Entity Type

Share Economy

Logo Text

LodVenra

Number of Pages Required

5+ page

Font styles to use
Sans Serif

Colors
3276b5

Requirements
Must have
• A messaging system whereby we can create direct communication between those offering rooms and those looking for rooms.
• A call to action that says " Schedule an Inspection"
• Landing page for promoting rooms
• A home page for showing stock.
• Profile page for those selling rooms
• Profile page for those looking for rooms.
• A scheduling calendar for booking inspections
Nice to have
• Pages where new residents can lock in a room.. pay bond and rents.. and sign contracts
• Notifications
• SMS capabilities in the backend.
Should not have
• No script or handwriting fonts.

```html
<!DOCTYPE html>
<html lang="en">
<head>
<meta charset="utf-8">
<title>Lodvenra – House-share and Room Rental</title>
<link href="https://fonts.googleapis.com/css2?family=Open+Sans:wght@400;600;700&family=Source+Sans+3:wght@400;600;700&display=swap" rel="stylesheet">
<style>
:root{
  --brand:#3276b5;
  --red:#f20d0d;
  --sky:#7ecdef;
  --ink:#333;
  --muted:#777;
  --light:#f6f7f9;
  --line:#e3e6ea;
  --gold:#f2a516;
  --dark-bar:rgba(40,44,54,.85);
}
*{box-sizing:border-box;margin:0;padding:0}
html,body{width:1200px;height:2826px;overflow:hidden}
body{font-family:"Open Sans",Arial,sans-serif;color:var(--ink);background:#fff;position:relative}
.section{position:absolute;left:0;width:1200px}
.btn{display:inline-block;background:var(--red);color:#fff;font-weight:700;font-size:12px;text-align:center;font-family:"Source Sans 3",Arial,sans-serif}

/* hero */
.hero{top:0;height:400px;overflow:hidden}
.hero-photo{position:absolute;inset:0;background:
  radial-gradient(ellipse 22% 30% at 50% 42%,rgba(255,236,190,.95),rgba(255,236,190,0) 100%),
  radial-gradient(ellipse 20% 26% at 74% 40%,rgba(250,214,150,.9),rgba(250,214,150,0) 100%),
  radial-gradient(ellipse 16% 40% at 8% 45%,rgba(46,62,34,.95),rgba(46,62,34,0) 100%),
  radial-gradient(ellipse 12% 34% at 95% 48%,rgba(70,78,48,.9),rgba(70,78,48,0) 100%),
  radial-gradient(ellipse 26% 16% at 60% 80%,rgba(70,150,210,.9),rgba(70,150,210,0) 100%),
  radial-gradient(ellipse 30% 14% at 40% 12%,rgba(60,82,112,.9),rgba(60,82,112,0) 100%),
  linear-gradient(180deg,#6a7296 0%,#a69a92 22%,#d9c39c 45%,#c9a877 62%,#8ea6b8 78%,#dfe7ee 88%)}
.hero-fade{position:absolute;left:0;right:0;bottom:0;height:120px;background:linear-gradient(180deg,rgba(255,255,255,0),rgba(255,255,255,.85) 45%,#fff 80%)}
.topbar{position:absolute;left:0;top:15px;width:1200px;height:38px;background:var(--dark-bar)}
.logo{position:absolute;left:250px;top:9px;color:#fff;font-family:"Source Sans 3",sans-serif;font-weight:700;font-size:16px}
.auth{position:absolute;left:798px;top:7px;height:24px;display:flex;align-items:center}
.auth .btn{height:24px;line-height:24px;padding:0 14px}
.auth .or{width:22px;height:22px;border-radius:50%;background:var(--brand);color:#fff;font-size:9px;font-weight:700;line-height:18px;text-align:center;margin:0 -4px;position:relative;z-index:1;border:2px solid #fff}
.hero-title{position:absolute;left:462px;top:196px;width:277px;height:54px;background:rgba(40,44,54,.85);color:#fff;text-align:center;padding-top:7px}
.hero-title h1{font-family:"Source Sans 3",sans-serif;font-size:16px;font-weight:700;letter-spacing:.3px}
.hero-title p{font-size:8px;line-height:10px;color:#ddd;margin-top:2px}
.search{position:absolute;left:250px;top:264px;width:701px;height:47px;background:#fff;box-shadow:0 2px 8px rgba(0,0,0,.12);display:flex;align-items:center}
.search .lead{width:228px;padding-left:10px;font-size:11px;font-weight:600;color:var(--brand);line-height:14px;border-right:1px solid var(--line)}
.search .opt{font-size:10px;color:#555;margin-left:14px;display:flex;align-items:center;gap:6px}
.search .dot{width:6px;height:6px;border-radius:50%;background:#555}
.search .ring{width:7px;height:7px;border-radius:50%;border:1px solid #999}
.search .field{margin-left:22px;width:130px;height:22px;border:1px solid var(--line);font-size:8px;color:#aaa;padding:5px 6px}
.search .btn{margin-left:18px;width:100px;height:24px;line-height:24px}

/* about */
.about{top:424px;height:270px}
.about h2{position:absolute;left:250px;top:50px;font-family:"Source Sans 3",sans-serif;font-size:16px;font-weight:700}
.about p{position:absolute;left:250px;top:78px;width:320px;font-size:9px;line-height:13px;color:var(--muted)}
.about .btn{position:absolute;left:250px;top:162px;width:97px;height:25px;line-height:25px}
.about-photo{position:absolute;left:608px;top:6px;width:343px;height:256px;background:
  radial-gradient(ellipse 16% 30% at 95% 22%,rgba(70,105,50,.85),rgba(70,105,50,0) 100%),
  radial-gradient(ellipse 26% 16% at 55% 22%,rgba(70,70,70,.55),rgba(70,70,70,0) 100%),
  radial-gradient(ellipse 40% 16% at 50% 62%,rgba(255,255,255,.95),rgba(255,255,255,0) 100%),
  radial-gradient(ellipse 22% 14% at 72% 66%,rgba(150,150,150,.7),rgba(150,150,150,0) 100%),
  linear-gradient(180deg,#eeeae4 0%,#f4f1ec 40%,#e3e0db 55%,#c9c6c0 75%,#6f6a64 92%,#3c3a38 100%)}

/* activities */
.activities{top:716px;height:420px;overflow:hidden}
.activities-photo{position:absolute;inset:0;background:
  radial-gradient(ellipse 14% 30% at 10% 25%,rgba(120,110,90,.45),rgba(120,110,90,0) 100%),
  radial-gradient(ellipse 16% 34% at 88% 30%,rgba(190,150,110,.45),rgba(190,150,110,0) 100%),
  radial-gradient(ellipse 30% 18% at 50% 55%,rgba(255,255,255,.7),rgba(255,255,255,0) 100%),
  linear-gradient(180deg,#d8d3c9 0%,#ece9e3 35%,#e5e2dc 58%,#b7dcee 75%,var(--sky) 88%)}
.activities h2{position:absolute;left:0;width:100%;top:34px;text-align:center;font-family:"Source Sans 3",sans-serif;font-size:19px;font-weight:700;color:#222}
.activity{position:absolute;width:320px;height:112px}
.activity .thumb{position:absolute;left:0;top:0;width:110px;height:110px;border-radius:50%;border:2px solid #e04a4a}
.t1{background:radial-gradient(circle at 50% 70%,#c89a5e,rgba(200,154,94,0) 45%),linear-gradient(160deg,#e9e5df,#cfc8be 50%,#7a6a55)}
.t2{background:radial-gradient(circle at 40% 75%,#1f3b4a,rgba(31,59,74,0) 40%),linear-gradient(160deg,#f2efe9,#d9d0c2 55%,#9a7f68)}
.t3{background:radial-gradient(circle at 55% 60%,#e9e6e0,rgba(233,230,224,0) 40%),linear-gradient(160deg,#4a4c50,#8b8680 50%,#2e2e30)}
.t4{background:radial-gradient(circle at 45% 70%,#e8b23a,rgba(232,178,58,0) 38%),linear-gradient(160deg,#f1eee8,#d6d2ca 55%,#8c857b)}
.activity h3{position:absolute;left:122px;top:14px;font-family:"Source Sans 3",sans-serif;font-size:16px;font-weight:600;color:#555;text-transform:uppercase;white-space:nowrap}
.activity p{position:absolute;left:122px;top:36px;width:195px;font-size:9px;line-height:12px;color:#555}
.activity .meta{position:absolute;left:122px;top:66px;display:flex;align-items:center;gap:14px;font-size:9px;color:#666}
.activity .meta span{display:flex;align-items:center;gap:4px}
.stars{color:var(--gold);font-size:11px;letter-spacing:1px}

/* contact form */
.enquiry{top:1130px;height:292px;background:var(--sky)}
.enquiry h2{position:absolute;left:0;width:100%;top:86px;text-align:center;font-family:"Source Sans 3",sans-serif;font-size:19px;font-weight:600;color:#fff}
.enquiry p{position:absolute;left:400px;width:400px;top:120px;text-align:center;font-size:9px;line-height:13px;color:#2c5f80}
.input{position:absolute;height:18px;border-bottom:1px solid #fff;color:#fff;font-size:10px;padding-left:2px}
.send{position:absolute;left:836px;top:212px;width:115px;height:25px;background:#fff;color:var(--brand);font-size:12px;font-weight:700;text-align:center;line-height:25px}

/* team */
.team{top:1422px;height:210px}
.member{position:absolute;top:38px;width:104px;text-align:center}
.member .avatar{width:104px;height:104px;border-radius:50%;border:2px solid #8fd2ec;padding:3px;background:#fff}
.member .avatar div{width:100%;height:100%;border-radius:50%}
.a1{background:radial-gradient(circle at 50% 45%,#b9896c,rgba(185,137,108,0) 35%),linear-gradient(180deg,#8ea9bd,#5e7c93 55%,#2f3b48)}
.a2{background:radial-gradient(circle at 50% 48%,#e6b492,rgba(230,180,146,0) 32%),linear-gradient(180deg,#7b4a2e,#b5622f 50%,#5a3320)}
.a3{background:radial-gradient(circle at 50% 45%,#c4937a,rgba(196,147,122,0) 30%),linear-gradient(180deg,#6f7f8f,#47535f 55%,#1f2630)}
.a4{background:radial-gradient(circle at 50% 48%,#e3b999,rgba(227,185,153,0) 32%),linear-gradient(180deg,#a08a70,#c9a57b 50%,#6e5744)}
.a5{background:radial-gradient(circle at 50% 45%,#d2a083,rgba(210,160,131,0) 32%),linear-gradient(180deg,#e4e4e2,#c7c5c2 55%,#6f655c)}
.member .name{margin-top:8px;font-size:12px;font-weight:600;color:#3aa0d8;letter-spacing:.5px}
.member .place{font-size:9px;color:#888}

/* worldwide band */
.worldwide{top:1632px;height:148px;background:var(--brand);color:#fff;text-align:center}
.worldwide h2{margin-top:22px;font-family:"Source Sans 3",sans-serif;font-size:16px;font-weight:700}
.worldwide p{font-size:9px;line-height:12px;margin:6px auto 0;width:400px}
.worldwide .note{margin-top:4px;font-weight:600}
.worldwide .btn{margin-top:10px;width:192px;height:24px;line-height:24px;font-size:11px}

/* blog */
.blog{top:1780px;height:386px;background:var(--light)}
.blog h2{position:absolute;left:0;width:100%;top:30px;text-align:center;font-family:"Source Sans 3",sans-serif;font-size:19px;font-weight:600;color:#222}
.rule{position:absolute;left:576px;width:48px;height:3px;background:var(--brand)}
.post{position:absolute;top:85px;width:220px;height:255px;background:#eef0f4}
.post .photo{height:108px}
.b1{background:radial-gradient(ellipse 30% 40% at 30% 55%,#d0475a,rgba(208,71,90,0) 100%),radial-gradient(ellipse 30% 40% at 72% 50%,#e8c9a8,rgba(232,201,168,0) 100%),linear-gradient(180deg,#a7b98a,#6f8a55 50%,#3d4a2e)}
.b2{background:radial-gradient(ellipse 30% 45% at 35% 55%,#8a5a3e,rgba(138,90,62,0) 100%),radial-gradient(ellipse 28% 40% at 68% 50%,#e1bc98,rgba(225,188,152,0) 100%),linear-gradient(180deg,#3b3a3a,#5d4a3e 50%,#2a2626)}
.b3{background:radial-gradient(ellipse 40% 30% at 50% 30%,#f3d9a0,rgba(243,217,160,0) 100%),radial-gradient(ellipse 30% 35% at 70% 65%,#c95a3c,rgba(201,90,60,0) 100%),linear-gradient(180deg,#b5845a,#8b5a3c 55%,#4d3326)}
.post h3{margin:10px 6px 0;font-family:"Source Sans 3",sans-serif;font-size:16px;font-weight:600;color:#555;white-space:nowrap}
.post .date{margin:6px 6px 0;font-size:8px;color:#444}
.post p{margin:6px 6px 0;font-size:8.6px;line-height:14px;color:#444;letter-spacing:-.1px}
.post .more{position:absolute;left:6px;bottom:8px;font-size:10px;color:var(--brand);font-weight:600}
.post .corner{position:absolute;right:0;bottom:0}

/* testimonials */
.testimonials{top:2166px;height:346px;overflow:hidden}
.testimonials-photo{position:absolute;inset:0;background:
  radial-gradient(ellipse 14% 18% at 20% 45%,rgba(250,210,140,.8),rgba(250,210,140,0) 100%),
  radial-gradient(ellipse 12% 16% at 80% 38%,rgba(250,210,140,.75),rgba(250,210,140,0) 100%),
  radial-gradient(ellipse 18% 25% at 6% 60%,rgba(60,70,85,.7),rgba(60,70,85,0) 100%),
  radial-gradient(ellipse 16% 25% at 94% 55%,rgba(60,70,85,.6),rgba(60,70,85,0) 100%),
  linear-gradient(180deg,#7f9cbf 0%,#a9b6c4 35%,#c6b9a4 58%,#e9e6e2 80%,#fff 92%)}
.testimonials h2{position:absolute;left:0;width:100%;top:18px;text-align:center;font-family:"Source Sans 3",sans-serif;font-size:19px;font-weight:600;color:#222}
.quote-card{position:absolute;left:320px;top:62px;width:562px;height:210px;background:rgba(255,255,255,.45)}
.quote-avatar{position:absolute;left:564px;top:70px;width:72px;height:72px;border-radius:50%;border:2px solid #fff;background:radial-gradient(circle at 50% 50%,#e8c3a3,rgba(232,195,163,0) 35%),linear-gradient(180deg,#d9b46a,#b98f55 50%,#6d5a48)}
.quote-mark{position:absolute;left:586px;top:132px}
.quote-name{position:absolute;left:0;width:100%;top:168px;text-align:center;font-size:13px;font-weight:600;color:#333}
.quote-text{position:absolute;left:400px;width:400px;top:186px;text-align:center;font-size:9px;line-height:12px;color:#444}
.quote-mark2{position:absolute;left:586px;top:238px}
.dots{position:absolute;left:588px;top:292px;display:flex;gap:4px}
.dots i{width:5px;height:5px;border-radius:50%;border:1px solid var(--brand);display:block}
.dots i.on{background:var(--brand)}

/* press */
.press{top:2540px;height:60px;display:flex;justify-content:center;align-items:center;gap:12px}
.press .seen{font-size:9px;font-weight:700;color:#aaa;line-height:10px;text-align:center;width:24px}
.press .badge{width:50px;height:36px;background:#d8d9dc}

/* footer */
.footer{top:2622px;height:180px;border-top:1px solid var(--line)}
.col{position:absolute;top:20px}
.col h4{font-family:"Source Sans 3",sans-serif;font-size:12px;font-weight:700;color:#222;margin-bottom:10px}
.col li{list-style:none;font-size:9px;color:#333;line-height:21.5px}
.contact-row{display:flex;align-items:center;gap:10px;font-size:9px;color:#333;margin-bottom:12px;line-height:12px}
.contact-row .ico{width:20px;height:20px;border-radius:50%;background:var(--brand);display:flex;align-items:center;justify-content:center;flex:none}
.bottombar{top:2801px;height:25px;background:var(--brand);color:#fff;font-size:8px;line-height:25px;padding-left:250px}
</style>
</head>
<body>

<header class="section hero">
  <div class="hero-photo" role="img" aria-label="Photo of a lit white villa with terrace, palms and pool at dusk"></div>
  <div class="hero-fade"></div>
  <div class="topbar">
    <div class="logo">Lodvenra</div>
    <div class="auth">
      <span class="btn">Log in</span><span class="or">OR</span><span class="btn">Sign up</span>
    </div>
  </div>
  <div class="hero-title">
    <h1>LIVE WITH PEOPLE YOU LIKE</h1>
    <p>Find a quality room in a well managed house<br>share with people who suit your way of life</p>
  </div>
  <form class="search">
    <div class="lead">Advertise your room in minutes or<br>find housemates with similar interests</div>
    <div class="opt"><span class="dot"></span>Need a room</div>
    <div class="opt"><span class="ring"></span>Advertise a rooms</div>
    <div class="field">postcode</div>
    <span class="btn">Search</span>
  </form>
</header>

<section class="section about">
  <h2>About Us</h2>
  <p>Lodvenra.com has Friends from around the world available for hire.<br>Rent a Friend to attend a social event, wedding, or party with you. Hire someone to introduce you to new people, or someone to go to a movie or a restaurant with. Hire a Friend to show you around a new town, teach you a new skill/hobby, or just someone for companionship.</p>
  <span class="btn">Read More</span>
  <div class="about-photo" role="img" aria-label="Photo of a bright bedroom with a made double bed, framed prints and a plant"></div>
</section>

<section class="section activities">
  <div class="activities-photo" role="img" aria-label="Soft background photo of a living room fading into sky blue"></div>
  <h2>People are using &nbsp;Lodvenra for all kinds of activities:</h2>

  <div class="activity" style="left:250px;top:107px">
    <div class="thumb t1" role="img" aria-label="Photo of a furnished living room"></div>
    <h3>Introduce you to people</h3>
    <p>Quisque at lacus in augue mattis facilisis id at tortor. Nam vel pharetra arcu.</p>
    <div class="meta"><span>▭ 2</span><span>◫ 2</span><span>▢ 1</span><span class="stars">★★★★★</span></div>
  </div>
  <div class="activity" style="left:639px;top:107px">
    <div class="thumb t2" role="img" aria-label="Photo of a bright bedroom"></div>
    <h3>Teaching manners</h3>
    <p>Quisque at lacus in augue mattis facilisis id at tortor. Nam vel pharetra arcu.</p>
    <div class="meta"><span>▭ 2</span><span>◫ 2</span><span>▢ 1</span><span class="stars">★★★★★</span></div>
  </div>
  <div class="activity" style="left:250px;top:239px">
    <div class="thumb t3" role="img" aria-label="Photo of a dark modern bedroom"></div>
    <h3>Friends with disabled</h3>
    <p>Quisque at lacus in augue mattis facilisis id at tortor. Nam vel pharetra arcu.</p>
    <div class="meta"><span>▭ 2</span><span>◫ 2</span><span>▢ 1</span><span class="stars">★★★★★</span></div>
  </div>
  <div class="activity" style="left:639px;top:239px">
    <div class="thumb t4" role="img" aria-label="Photo of a lounge with a yellow sofa"></div>
    <h3>Going to park</h3>
    <p>Quisque at lacus in augue mattis facilisis id at tortor. Nam vel pharetra arcu.</p>
    <div class="meta"><span>▭ 2</span><span>◫ 2</span><span>▢ 1</span><span class="stars">★★★★★</span></div>
  </div>
</section>

<section class="section enquiry">
  <h2>Available House-share and Room for Rental</h2>
  <p>Quisque at lacus in augue mattis facilisis id at tortor. Nam vel pharetra arcu. Proin sit amet metus turpis. Cras nec felis sollicitudin, pulvinar velit id, viverra dui.</p>
  <div class="input" style="left:250px;top:178px;width:165px">Name</div>
  <div class="input" style="left:428px;top:178px;width:165px">Email</div>
  <div class="input" style="left:606px;top:178px;width:165px">Phone</div>
  <div class="input" style="left:784px;top:178px;width:167px">Services</div>
  <div class="input" style="left:250px;top:216px;width:523px">Message</div>
  <div class="send">Send</div>
</section>

<section class="section team">
  <div class="member" style="left:249px"><div class="avatar"><div class="a1" role="img" aria-label="Portrait photo of Noah"></div></div><div class="name">NOAH</div><div class="place">United Kingdom</div></div>
  <div class="member" style="left:400px"><div class="avatar"><div class="a2" role="img" aria-label="Portrait photo of Ciara"></div></div><div class="name">CIARA</div><div class="place">United Kingdom</div></div>
  <div class="member" style="left:549px"><div class="avatar"><div class="a3" role="img" aria-label="Portrait photo of Liam"></div></div><div class="name">LIAM</div><div class="place">United Kingdom</div></div>
  <div class="member" style="left:698px"><div class="avatar"><div class="a4" role="img" aria-label="Portrait photo of Shelby"></div></div><div class="name">SHELBY</div><div class="place">United Kingdom</div></div>
  <div class="member" style="left:847px"><div class="avatar"><div class="a5" role="img" aria-label="Portrait photo of William"></div></div><div class="name">WILLIAM</div><div class="place">United Kingdom</div></div>
</section>

<section class="section worldwide">
  <h2>Lodvenra.com is Available Worldwide!</h2>
  <p>It's always good to have a local Friend no matter where you go. Are you moving to a new city, travel for work, or going on vacation? Hire a local Friend to show you around a new town!</p>
  <p class="note">Learn the best places for shopping, eating, entertainment, hotels and more.</p>
  <span class="btn">Click here to Start Free Search Now</span>
</section>

<section class="section blog">
  <h2>Our Blog</h2>
  <div class="rule" style="top:62px"></div>
  <article class="post" style="left:250px">
    <div class="photo b1" role="img" aria-label="Photo of two friends laughing together outdoors"></div>
    <h3>Typesetting Industry</h3>
    <div class="date">31 March 2017</div>
    <p>Lorem Ipsum is simply dummy text of the printing and typesetting industry. Lorem Ipsum has been the industry's standard dummy text ever since the 1500s, when an unknown printer took a galley of type and</p>
    <span class="more">Read More</span>
    <svg class="corner" width="10" height="10"><path d="M10 0V10H0Z" fill="#3276b5"/></svg>
  </article>
  <article class="post" style="left:491px">
    <div class="photo b2" role="img" aria-label="Photo of two friends sharing a hug"></div>
    <h3>Etiam faucibus ut sem.</h3>
    <div class="date">31 March 2017</div>
    <p>Lorem Ipsum is simply dummy text of the printing and typesetting industry. Lorem Ipsum has been the industry's standard dummy text ever since the 1500s, when an unknown printer took a galley of type and</p>
    <span class="more">Read More</span>
    <svg class="corner" width="10" height="10"><path d="M10 0V10H0Z" fill="#3276b5"/></svg>
  </article>
  <article class="post" style="left:731px">
    <div class="photo b3" role="img" aria-label="Photo of friends dining together at a table"></div>
    <h3>Praesent ac maximus tortor</h3>
    <div class="date">31 March 2017</div>
    <p>Lorem Ipsum is simply dummy text of the printing and typesetting industry. Lorem Ipsum has been the industry's standard dummy text ever since the 1500s, when an unknown printer took a galley of type and</p>
    <span class="more">Read More</span>
    <svg class="corner" width="10" height="10"><path d="M10 0V10H0Z" fill="#3276b5"/></svg>
  </article>
</section>

<section class="section testimonials">
  <div class="testimonials-photo" role="img" aria-label="Soft background photo of a lit family house at dusk"></div>
  <h2>TESTIMONIALS</h2>
  <div class="rule" style="top:48px"></div>
  <div class="quote-card"></div>
  <div class="quote-avatar" role="img" aria-label="Portrait photo of Mara Velden"></div>
  <svg class="quote-mark" width="28" height="22" viewBox="0 0 28 22"><path d="M2 22V12C2 5 6 1 12 0V5C8 6 7 9 7 12H12V22ZM16 22V12C16 5 20 1 26 0V5C22 6 21 9 21 12H26V22Z" fill="#e64b4b"/></svg>
  <div class="quote-name">Mara Velden</div>
  <p class="quote-text">Lorem Ipsum is simply dummy text of the printing and typesetting industry. Lorem Ipsum has been the industry's standard dummy text ever since the 1500s, when an unknown printer took. Lorem Ipsum is simply dummy text of the printing and typesetting industry.</p>
  <svg class="quote-mark2" width="28" height="22" viewBox="0 0 28 22"><path d="M2 22V12C2 5 6 1 12 0V5C8 6 7 9 7 12H12V22ZM16 22V12C16 5 20 1 26 0V5C22 6 21 9 21 12H26V22Z" fill="#f0a0a0"/></svg>
  <div class="dots"><i class="on"></i><i></i><i></i></div>
</section>

<section class="section press">
  <div class="seen">AS SEEN ON</div>
  <div class="badge"></div><div class="badge"></div><div class="badge"></div><div class="badge"></div><div class="badge"></div><div class="badge"></div><div class="badge"></div>
</section>

<footer class="section footer">
  <div class="col" style="left:250px"><h4>QUICK LINKS</h4><ul><li>Latest Stories</li><li>Press Releases</li><li>Media Inquiries</li><li>Media Partners</li><li>The News</li></ul></div>
  <div class="col" style="left:396px"><h4>SUPPORT</h4><ul><li>Latest Stories</li><li>Press Releases</li><li>Media Inquiries</li><li>Media Partners</li><li>The News</li></ul></div>
  <div class="col" style="left:541px"><h4>EVENT</h4><ul><li>Latest Stories</li><li>Press Releases</li><li>Media Inquiries</li><li>Media Partners</li><li>The News</li></ul></div>
  <div class="col" style="left:665px"><h4>NEWS &amp; MEDIA</h4><ul><li>Submit Your Story</li><li>Member Updates Archive</li><li>Contact</li><li>Login</li></ul></div>
  <div class="col" style="left:823px"><h4>CONTACT US</h4>
    <div class="contact-row"><span class="ico"><svg width="10" height="10" viewBox="0 0 10 10"><path d="M2 0L4 2.5 3 3.8C3.7 5.3 4.7 6.3 6.2 7L7.5 6 10 8 8.5 10C4 9.5 .5 6 0 1.5Z" fill="#fff"/></svg></span>+90 555 014 27 63</div>
    <div class="contact-row"><span class="ico"><svg width="10" height="8" viewBox="0 0 10 8"><rect width="10" height="8" fill="#fff"/><path d="M0 0L5 4.5 10 0" stroke="#3276b5" fill="none"/></svg></span>info@lodvenra.com</div>
    <div class="contact-row"><span class="ico"><svg width="8" height="11" viewBox="0 0 8 11"><path d="M4 11C4 11 0 6.5 0 4A4 4 0 0 1 8 4C8 6.5 4 11 4 11Z" fill="#fff"/><circle cx="4" cy="4" r="1.5" fill="#3276b5"/></svg></span>Velmora Sanayi Yolu<br>45990 Ardenköy</div>
  </div>
</footer>
<div class="section bottombar">© Copyrights 2018 Lodvenra | All rights reserved.</div>

</body>
</html>
```